Hello Creative Minds!
Our business is after a elegant and classy flyer that draws attention!
The business is Velmora Turf - Lawn Rejuvenation Services. We provide services that maintain a healthy and vibrant green lawn through the tough Australian seasons. The products we use limits the water needed to keep grass green to a minimum - practically none at all! This not only helps the home owner or home seller but the environment by limiting the use of water that is needed to create a green lawn. The products we use are made from natural ingredients that are and pet friendly.
This fly will be our introductory offer to the market. Below are the required points that need to be on the flyer. Attached is the business logo, before & after pictures and 1 example of the LAYOUT not DESIGN of what the flyer should be laid out like or similar to. Feel free to use different 'Lawn Mower' pictures.
All the best; if you need any questions answered please feel free to message.
REQUIRED POINTS (Please re-phrase were possible);
*Instantly restores the natural green colour of grass – year round
*Lasts for up to 3 months
*Substantially reduces watering needs
*Pet friendly
*Stays green during droughts and water restrictions
*UV fade resistant
*Won’t bleed, run, or stain once absorbed into the grass
*Safe for the environment, pets and people
*Works in extreme heat, cold and frost
*Organic and natural – no harmful chemicals
*Reduces the amount of fertilizer
and water used on lawns
*Kerb appeal is essential for getting your property sold for the highest price possible
SERVICES & PRICING
Lawn maintenance (cut & trim) starting from $60
Lawn rejuvenation starting from $80 (Only $27 a month for 3 months)*
Package deal starting from $120
Introductory offer: 25% off all services. Refer a friend, when they book you receive another 25% off your next service.
LOCATIONS
Nowra to Sydney
CONTACT NUMBER
Will be posted with the winner - please leave an area for this.
SOCIAL MEDIA
Please add Chatterloop and Snapvista logo's
Updates
Competition has finished, thank you to all that have participated! I will review and comment on the flyers that need assistance. All the best with future designs!
Target Market(s)
home owners, home sellers, property developers, real estates and nursing homes and government housing.
Industry/Entity Type
Lawn Care
Look and feel
Each slider illustrates characteristics of the customer's brand and the style your logo design should communicate.

```html
<!DOCTYPE html>
<html lang="en">
<head>
<meta charset="utf-8">
<title>Velmora Turf – Lawn Rejuvenation Services Flyer</title>
<link rel="stylesheet" href="https://fonts.googleapis.com/css2?family=Barlow:wght@400;500&family=Barlow+Condensed:wght@400;500&family=Bebas+Neue&family=Oswald:wght@700&display=swap">
<style>
  :root {
    --page-bg: #dfe4ea;
    --deep-green: #2f9058;
    --heading-green: #2a8a55;
    --lime: #a8cd55;
    --lime-light: #bcdc72;
    --photo-dark: #3f8a3a;
    --photo-light: #7cbf5a;
    --mist: #dfe3dc;
    --paper: #f2f1f4;
    --ink: #2d2d2d;
    --tag-red: #cc3442;
    --tag-red-dark: #a82632;
    --white: #ffffff;
  }
  * { margin: 0; padding: 0; box-sizing: border-box; }
  html, body { width: 1200px; height: 943px; overflow: hidden; }
  body { background: var(--page-bg); font-family: "Barlow", sans-serif; color: var(--ink); }

  .flyer {
    position: absolute; left: 268px; top: 20px;
    width: 663px; height: 903px;
    background: var(--paper);
    overflow: hidden;
    box-shadow: 0 4px 18px rgba(0,0,0,.18);
  }
  .flyer__shapes { position: absolute; inset: 0; }

  .brand { position: absolute; left: 26px; top: 236px; width: 305px; text-align: center; color: var(--white); }
  .brand__name { font-family: "Barlow", sans-serif; font-weight: 500; font-size: 38px; line-height: 46px; letter-spacing: 1px; }
  .brand__tagline { font-size: 8px; line-height: 10px; letter-spacing: 3.5px; margin-top: 20px; }

  .benefit { position: absolute; white-space: nowrap; }
  .benefit__title {
    font-family: "Bebas Neue", sans-serif; font-weight: 400; font-size: 16px; line-height: 15px;
    color: var(--heading-green); letter-spacing: .3px;
    display: flex; align-items: center; gap: 9px;
  }
  .benefit__title svg { width: 8px; height: 11px; flex: none; }
  .benefit__text { font-size: 9.8px; line-height: 13px; margin: 4px 0 0 35px; }
  .benefit--plain .benefit__title { padding-left: 17px; }
  .benefit--right .benefit__text { margin-left: 30px; }
  .benefit__indent { padding-left: 15px; }

  .offer { position: absolute; left: 95px; top: 700px; display: flex; align-items: flex-start;
    font-family: "Oswald", sans-serif; font-weight: 700; color: var(--tag-red);
    text-shadow: 2px 3px 0 var(--tag-red-dark); }
  .offer__figure { font-size: 70px; line-height: 74px; letter-spacing: -2px; }
  .offer__unit { display: flex; flex-direction: column; align-items: center; margin-left: 2px; }
  .offer__percent { font-size: 34px; line-height: 36px; }
  .offer__off { font-size: 30px; line-height: 32px; margin-top: -2px; }
  .offer__note {
    position: absolute; left: 30px; top: 788px;
    font-family: "Barlow Condensed", sans-serif; font-size: 13.5px; line-height: 15px; color: var(--ink);
    white-space: nowrap;
  }

  .price-tag {
    position: absolute; left: 377px; width: 248px; height: 54px;
    color: var(--white); display: flex; align-items: center;
    font-family: "Barlow Condensed", sans-serif;
  }
  .price-tag__from { width: 97px; text-align: center; }
  .price-tag__from span { display: block; font-size: 8.5px; line-height: 10px; }
  .price-tag__from strong { display: block; font-weight: 400; font-size: 20px; line-height: 22px; }
  .price-tag__from em { display: block; font-style: normal; font-size: 5px; line-height: 6px; }
  .price-tag__rule { width: 1px; height: 40px; background: var(--white); }
  .price-tag__service { padding-left: 12px; font-size: 11.5px; letter-spacing: .3px; line-height: 12px; }
  .price-tag__service ul { list-style: none; font-size: 7px; line-height: 10px; margin: 3px 0 0 10px; }
  .price-tag--list { align-items: flex-start; padding-top: 7px; }
  .price-tag--list .price-tag__rule { margin-top: 0; }

  .footer { position: absolute; left: 0; right: 0; top: 862px; height: 41px; color: var(--white);
    font-family: "Barlow Condensed", sans-serif; }
  .footer__area { position: absolute; left: 40px; top: 12px; font-size: 17px; line-height: 20px; letter-spacing: .5px; }
  .footer__phone { position: absolute; left: 240px; top: 6px; display: flex; align-items: center; gap: 8px;
    font-size: 27px; line-height: 32px; letter-spacing: .5px; }
  .footer__phone svg { width: 24px; height: 24px; }
  .footer__social { position: absolute; left: 455px; top: 8px; font-size: 11.5px; line-height: 15px; list-style: none; white-space: nowrap; }
</style>
</head>
<body>
<main class="flyer">
  <svg class="flyer__shapes" viewBox="0 0 663 903" width="663" height="903">
    <defs>
      <linearGradient id="heroFill" x1="0" y1="0" x2="1" y2="1">
        <stop offset="0" stop-color="var(--photo-light)"/>
        <stop offset="1" stop-color="var(--photo-dark)"/>
      </linearGradient>
      <linearGradient id="bandFade" x1="0" y1="0" x2="1" y2="0">
        <stop offset="0" stop-color="var(--deep-green)" stop-opacity="1"/>
        <stop offset=".45" stop-color="var(--deep-green)" stop-opacity="1"/>
        <stop offset=".8" stop-color="var(--deep-green)" stop-opacity="0"/>
      </linearGradient>
      <linearGradient id="bandMaskFade" x1="0" y1="0" x2="0" y2="1">
        <stop offset="0" stop-color="#fff" stop-opacity="0"/>
        <stop offset=".35" stop-color="#fff" stop-opacity="1"/>
      </linearGradient>
      <mask id="bandMask"><rect x="0" y="200" width="663" height="160" fill="url(#bandMaskFade)"/></mask>
      <clipPath id="heroClip">
        <path d="M0 0 H663 V290 C635 275 590 250 527 250 C400 250 320 320 240 338 C160 345 90 325 0 292 Z"/>
      </clipPath>
      <linearGradient id="beforeAfter" x1="0" y1="0" x2="0" y2="1">
        <stop offset="0" stop-color="#b9b48c"/>
        <stop offset=".5" stop-color="#c6c29f"/>
        <stop offset=".5" stop-color="#5a9a3e"/>
        <stop offset="1" stop-color="#3f7d2c"/>
      </linearGradient>
      <linearGradient id="yardBeforeAfter" x1="0" y1="0" x2="0" y2="1">
        <stop offset="0" stop-color="#9a9a96"/>
        <stop offset=".55" stop-color="#7d7d7a"/>
        <stop offset=".55" stop-color="#4f8f3c"/>
        <stop offset="1" stop-color="#3c6f2d"/>
      </linearGradient>
      <linearGradient id="footerGrass" x1="0" y1="0" x2="0" y2="1">
        <stop offset="0" stop-color="var(--lime-light)" stop-opacity="0"/>
        <stop offset=".4" stop-color="var(--lime-light)" stop-opacity="1"/>
        <stop offset="1" stop-color="var(--lime)"/>
      </linearGradient>
    </defs>

    <rect class="mist-field" x="0" y="260" width="663" height="370" fill="var(--mist)" role="img" aria-label="Soft close-up of lush grass blades"/>

    <g clip-path="url(#heroClip)">
      <rect class="hero-photo" x="0" y="0" width="663" height="360" fill="url(#heroFill)" role="img" aria-label="Photo of a person pushing a lawn mower across a green lawn"/>
      <rect class="brand-band" x="0" y="200" width="663" height="160" fill="url(#bandFade)" mask="url(#bandMask)"/>
    </g>

    <path class="wave-lime" d="M0 292 C90 325 160 345 240 338 C320 320 400 250 527 250 C590 250 635 275 663 290 L663 308 C635 292 590 270 527 270 C400 270 300 345 240 358 C150 365 80 338 0 312 Z" fill="var(--lime)"/>

    <path class="wave-paper" d="M0 540 C70 575 130 615 200 617 C280 619 320 565 380 545 C450 523 560 513 663 515 L663 903 L0 903 Z" fill="var(--paper)"/>
    <path class="wave-lower-lime" d="M0 530 C70 565 130 605 200 607 C280 609 320 555 380 535 C450 513 560 503 663 505 L663 515 C560 513 450 523 380 545 C320 565 280 619 200 617 C130 615 70 575 0 540 Z" fill="var(--lime)"/>

    <circle cx="166" cy="605" r="71" fill="url(#beforeAfter)" stroke="var(--lime)" stroke-width="5" role="img" aria-label="Before and after photo of dry grass turned green"/>
    <circle cx="378" cy="541" r="71" fill="url(#yardBeforeAfter)" stroke="var(--lime)" stroke-width="5" role="img" aria-label="Before and after photo of a backyard lawn"/>
    <g font-family="Bebas Neue, sans-serif" font-size="20" fill="var(--white)" text-anchor="middle">
      <text x="166" y="572">BEFORE</text>
      <text x="166" y="668">AFTER</text>
      <text x="378" y="508">BEFORE</text>
      <text x="378" y="604">AFTER</text>
    </g>

    <path class="tag-1" d="M377 638 H626 L614 664 L626 691 H377 Z" fill="var(--tag-red)"/>
    <rect class="tag-2" x="377" y="709" width="248" height="55" fill="var(--tag-red)"/>
    <rect class="tag-3" x="377" y="779" width="248" height="54" fill="var(--tag-red)"/>

    <rect class="footer-band" x="0" y="828" width="663" height="75" fill="url(#footerGrass)" role="img" aria-label="Grass blade border"/>
  </svg>

  <div class="brand">
    <div class="brand__name">Velmora Turf</div>
    <div class="brand__tagline">LAWN REJUVENATION SERVICES</div>
  </div>

  <section class="benefit" style="left:26px;top:378px;">
    <h3 class="benefit__title"><svg viewBox="0 0 8 11"><path d="M1 1 L6 5.5 L1 10" fill="none" stroke="var(--heading-green)" stroke-width="1.6"/></svg>INSTANT COLOUR</h3>
    <p class="benefit__text">Instantly restores the natural green colour of<br>your lawn, year-round.</p>
  </section>
  <section class="benefit" style="left:26px;top:431px;">
    <h3 class="benefit__title"><svg viewBox="0 0 8 11"><path d="M1 1 L6 5.5 L1 10" fill="none" stroke="var(--heading-green)" stroke-width="1.6"/></svg>LONGEVITY</h3>
    <p class="benefit__text">Stays green for up to 3 months per application,<br>even during droughts / water restriction periods.</p>
  </section>
  <section class="benefit benefit--plain" style="left:26px;top:492px;">
    <h3 class="benefit__title">SAFETY</h3>
    <p class="benefit__text">Being 100% eco-friendly and non-toxic</p>
  </section>

  <section class="benefit benefit--right" style="left:370px;top:311px;">
    <h3 class="benefit__title"><svg viewBox="0 0 8 11"><path d="M1 1 L6 5.5 L1 10" fill="none" stroke="var(--heading-green)" stroke-width="1.6"/></svg>NO MESS</h3>
    <p class="benefit__text">Won't wash off, run, stain or bleed once absorbed<br>into the grass.</p>
  </section>
  <section class="benefit benefit--right" style="left:370px;top:363px;">
    <h3 class="benefit__title"><svg viewBox="0 0 8 11"><path d="M1 1 L6 5.5 L1 10" fill="none" stroke="var(--heading-green)" stroke-width="1.6"/></svg>DURABILITY</h3>
    <p class="benefit__text">Works in extreme heat, cold and frosty climates,<br>AND works on ALL grass types.</p>
  </section>
  <section class="benefit benefit--right" style="left:370px;top:420px;">
    <h3 class="benefit__title"><svg viewBox="0 0 8 11"><path d="M1 1 L6 5.5 L1 10" fill="none" stroke="var(--heading-green)" stroke-width="1.6"/></svg>LESS WATERING &amp; FERTILISING</h3>
    <p class="benefit__text">drastically reduces the need to water and fertilise<br>your lawn in periods of drought,<br><span class="benefit__indent">helping you save water.</span></p>
  </section>

  <div class="price-tag price-tag--list" style="top:638px;">
    <div class="price-tag__from"><span>STARTING FROM</span><strong>60$</strong></div>
    <div class="price-tag__rule"></div>
    <div class="price-tag__service">LAWN MAINTENANCE<ul><li>&gt; CUT</li><li>&gt; TRIM</li></ul></div>
  </div>
  <div class="price-tag" style="top:709px;">
    <div class="price-tag__from"><span>STARTING FROM</span><strong>80$</strong><em>(ONLY $27 A MONTH FOR 3 MONTHS)</em></div>
    <div class="price-tag__rule"></div>
    <div class="price-tag__service">LAWN REJUVENATION</div>
  </div>
  <div class="price-tag" style="top:779px;">
    <div class="price-tag__from"><span>STARTING FROM</span><strong>120$</strong></div>
    <div class="price-tag__rule"></div>
    <div class="price-tag__service" style="padding-left:24px">PACKAGE DEAL</div>
  </div>

  <div class="offer">
    <span class="offer__figure">25</span>
    <span class="offer__unit"><span class="offer__percent">%</span><span class="offer__off">OFF</span></span>
  </div>
  <p class="offer__note">IF YOU REFER A FRIEND, WHEN THEY BOOK<br>YOU RECEIVE ANOTHER 25% OFF YOUR NEXT SERVICE</p>

  <footer class="footer">
    <span class="footer__area">NOWRA TO SYDNEY</span>
    <span class="footer__phone">
      <svg viewBox="0 0 24 24"><path d="M6.6 2.5 L9.5 6.8 L7.6 9.2 C8.8 11.8 11.3 14.4 14.6 16.2 L16.9 14.3 L21.3 17.2 L19.6 20.8 C12 21 3.2 12.6 3 4.2 Z" fill="none" stroke="var(--white)" stroke-width="1.6" stroke-linejoin="round"/></svg>
      0198765432
    </span>
    <ul class="footer__social">
      <li>Chatterloop /VELMORA TURF</li>
      <li>Snapvista /VELMORA TURF</li>
    </ul>
  </footer>
</main>
</body>
</html>
```